Laser Tattoo Removal Business Cards

We are looking for a professional business card design for a laser tattoo removal business. Ideally looking for a black business card design. The name of the business is Lumen Ink Clearing. We place our cards at local tattoo shops so we ideally are looking for something trendy/edgy to draw both male and female clientele in.

Target Market(s)

Male/Female ages 18-60

Contact Information for Business Card

black background ideally.. hoping to stay within greys, whites and black

Font styles to use
Serif
Sans Serif

Colors
121212
a9a9a9
5c5c5c
f5f5f5
ffffff
7f7f7f
606060
848484
9d9d9d

Requirements
Must have
• Employee Info:
• Marisol Dunmore
• Chief Executive Offer
• m: 919.555.0143
• w: 919.555.0178
• f: 919.555.0192
• mdunmore@lumeninkclearing.com
• Address:
• 4185 Fenwick Pkwy, Suite 210
• Raleigh, NC 27617
• Website:
• www.lumeninkclearing.com
Nice to have
• Myabe business name on back or logo on back and employee info on the front

```html
<!DOCTYPE html>
<html lang="en">
<head>
<meta charset="utf-8">
<title>Lumen Ink Clearing — Business Cards</title>
<link rel="stylesheet" href="https://fonts.googleapis.com/css2?family=Mulish:wght@400;700&display=swap">
<style>
  :root {
    --backdrop: #1e1e1e;
    --card: #121212;
    --ink: #f5f5f5;
    --ink-strong: #ffffff;
    --ink-muted: #a9a9a9;
    --rule: #848484;
  }
  * { box-sizing: border-box; margin: 0; padding: 0; }
  html, body {
    width: 1200px;
    height: 900px;
    overflow: hidden;
    background: var(--backdrop);
    font-family: "Mulish", sans-serif;
    color: var(--ink);
  }
  .canvas {
    position: relative;
    width: 1200px;
    height: 900px;
  }
  .card {
    position: absolute;
    left: 320px;
    width: 560px;
    height: 320px;
    background: var(--card);
    box-shadow: 0 10px 30px rgba(0,0,0,.45);
  }
  .card--front { top: 110px; }
  .card--back  { top: 470px; }

  /* Front */
  .brand {
    position: absolute;
    top: 92px;
    left: 0;
    right: 0;
    display: flex;
    align-items: center;
    justify-content: center;
    gap: 14px;
  }
  .brand__dot {
    width: 12px;
    height: 12px;
    border-radius: 50%;
    background: var(--ink-strong);
  }
  .brand__name {
    font-weight: 700;
    font-size: 34px;
    letter-spacing: 3px;
    text-transform: uppercase;
    color: var(--ink-strong);
  }
  .brand__rule {
    position: absolute;
    top: 150px;
    left: 190px;
    right: 190px;
    height: 1px;
    background: var(--rule);
  }
  .address {
    position: absolute;
    bottom: 50px;
    left: 0;
    right: 0;
    text-align: center;
    font-size: 17px;
    color: var(--ink);
  }

  /* Back */
  .person {
    position: absolute;
    top: 96px;
    right: 330px;
    text-align: right;
  }
  .person__name {
    font-weight: 700;
    font-size: 20px;
    letter-spacing: .5px;
    text-transform: uppercase;
    color: var(--ink-strong);
  }
  .person__title {
    font-size: 15px;
    color: var(--ink);
    margin-top: 2px;
  }
  .divider {
    position: absolute;
    top: 92px;
    left: 248px;
    width: 1px;
    height: 96px;
    background: var(--rule);
  }
  .phones {
    position: absolute;
    top: 106px;
    left: 272px;
    list-style: none;
  }
  .phones li {
    display: flex;
    align-items: center;
    gap: 10px;
    font-size: 17px;
    line-height: 24px;
    color: var(--ink);
  }
  .phones svg { width: 14px; height: 14px; fill: var(--ink); }
  .web {
    position: absolute;
    top: 222px;
    right: 200px;
    text-align: right;
    font-size: 16px;
    line-height: 22px;
    color: var(--ink);
  }
</style>
</head>
<body>
<main class="canvas">
  <section class="card card--front" aria-label="Card front">
    <div class="brand">
      <span class="brand__dot"></span>
      <span class="brand__name">Lumen Ink Clearing</span>
    </div>
    <div class="brand__rule"></div>
    <p class="address">4185 Fenwick Pkwy, Suite 210 Raleigh, NC 27617</p>
  </section>

  <section class="card card--back" aria-label="Card back">
    <div class="person">
      <h1 class="person__name">Marisol Dunmore</h1>
      <p class="person__title">Chief Executive Officer</p>
    </div>
    <div class="divider"></div>
    <ul class="phones">
      <li>
        <svg viewBox="0 0 14 14" aria-label="mobile"><path d="M4 0h6a1.5 1.5 0 0 1 1.5 1.5v11A1.5 1.5 0 0 1 10 14H4a1.5 1.5 0 0 1-1.5-1.5v-11A1.5 1.5 0 0 1 4 0zm0 1.5v9.5h6V1.5zM7 11.7a.8.8 0 1 0 0 1.6.8.8 0 0 0 0-1.6z"/></svg>
        919.555.0143
      </li>
      <li>
        <svg viewBox="0 0 14 14" aria-label="phone"><path d="M3 .5l2.2 2.8-1.3 1.8a8 8 0 0 0 5 5l1.8-1.3 2.8 2.2-1.3 2.3C6.5 13.3.7 7.5.7 1.8z"/></svg>
        919.555.0178
      </li>
      <li>
        <svg viewBox="0 0 14 14" aria-label="fax"><path d="M3.5 0h7v4h-7zM1 5h12a1 1 0 0 1 1 1v5h-2.5v3h-9v-3H0V6a1 1 0 0 1 1-1zm3.5 5v2.5h5V10z"/></svg>
        919.555.0192
      </li>
    </ul>
    <div class="web">
      <p>mdunmore@lumeninkclearing.com</p>
      <p>www.lumeninkclearing.com</p>
    </div>
  </section>
</main>
</body>
</html>
```